Single Page/Scrolling Design for Model Recruitment site

We need a design (and if you are capable, coding) for our company, Brimwell Parlour (LA as in Los Angeles). We like modern single page designs, hence the title for the project. We have already had a designer come up with a logo, which is attached. You're free to play around with the colors, although we want the site to have a feminine appeal to it.

The site is basically a recruitment project for girls who are interested in working as chat hosts for cam sites. We don't want anything cheesy that feels like a porn site. The inspiration for the logo (and the inspiration for the site) comes from the French and English salons of the late 18th century, where beautiful and intelligent women would gather to discuss a range of topics. We want the website to convey that this work is fun and exciting. Please keep these things in mind for the design.

As I mentioned, we like the modern look and feel of single page designs, especially because we don't have a ton of content. We just need an "About us" area, a "Work from Home" area, a "Work at The Brimwell Parlour" area, and "Contact Us" area which should have text boxes for entering email, subject, a message, etc.

The logo I mentioned is attached, as well as a very crude mockup of the layout of all the content I described.

Target Market(s)

Women age 18-35.

Industry/Entity Type

It Company

Font styles to use
Serif
Decorative
Script

Colors

Designer to choose colors to be used in the design.

Requirements
Should not have
• Images that are super sexual or even slightly pornographic. We want this to appeal to a broad range of women.

```html
<!DOCTYPE html>
<html lang="en">
<head>
<meta charset="utf-8">
<title>Brimwell Parlour</title>
<link rel="stylesheet" href="https://fonts.googleapis.com/css2?family=Questrial&family=Open+Sans:wght@400&display=swap">
<style>
:root{
  --pink:#d51b7c;
  --pink-deep:#8e0f52;
  --white:#ffffff;
  --ink:#1d1d1d;
  --grey-text:#8a8a8a;
  --field-text:#a5a5a5;
  --footer:#2a2a2a;
  --heading:'Questrial', sans-serif;
  --body:'Open Sans', sans-serif;
  --nav:Arial, Helvetica, sans-serif;
}
*{box-sizing:border-box;margin:0;padding:0}
html,body{width:700px;height:1200px;overflow:hidden}
body{position:relative;background:var(--white);font-family:var(--body);color:var(--ink)}
.page{position:relative;width:700px;height:1200px;overflow:hidden}

.site-nav{position:absolute;left:0;top:0;width:700px;height:40px;background:var(--pink);box-shadow:0 2px 4px rgba(0,0,0,.25);z-index:2;display:flex;justify-content:space-between;align-items:center;padding:0 132px 0 106px}
.site-nav a{font-family:var(--nav);font-size:9px;color:var(--white);text-decoration:none;letter-spacing:.1px;white-space:nowrap}

.hero{position:absolute;left:0;top:40px;width:700px;height:248px;overflow:hidden}
.hero-photo{position:absolute;inset:0;background:radial-gradient(circle at 70% 30%,#c98a6a 0,#8a3a26 35%,#3b1a12 75%)}
.hero-panel{position:absolute;inset:0}
.brand-mark{position:absolute;left:133px;top:18px;width:80px;height:80px;border-radius:50%;background:var(--pink)}
.brand-name{position:absolute;left:106px;top:104px;width:134px;text-align:center;font-family:var(--heading);font-size:12px;color:var(--pink)}
.hero-title{position:absolute;left:117px;top:136px;font-family:var(--heading);font-weight:400;font-size:22px;line-height:27px;color:var(--ink);white-space:nowrap}
.hero-sub{position:absolute;left:117px;top:191px;width:152px;font-family:var(--body);font-size:11.5px;line-height:14px;color:var(--ink)}
.hero-arrow{position:absolute;top:122px}

.band{position:absolute;left:0;width:700px;text-align:center}
.band h2{font-family:var(--heading);font-weight:400;font-size:17px}
.band p{width:490px;margin:0 auto;text-align:left;font-size:6.6px;line-height:12px}
.band-pink{background:var(--pink);color:var(--white)}
.about{top:288px;height:151px}
.about h2{margin-top:37px}
.about p{margin-top:14px}

.train{top:439px;height:177px;background:linear-gradient(90deg,#f3f3f4,#e9e9eb 60%,#efeff0)}
.train-photo{position:absolute;left:0;top:0;width:700px;height:177px;background:radial-gradient(ellipse at 62% 55%,#d9d9dc 0,rgba(233,233,235,0) 60%)}
.train h2{position:relative;margin-top:62px;color:var(--ink)}
.train p{position:relative;margin-top:13px;color:var(--grey-text)}

.work{top:616px;height:228px}
.work h2{margin-top:30px}
.work p{margin-top:12px}
.bubble{position:absolute;top:126px;width:72px;height:72px;border-radius:50%;background:var(--white);box-shadow:3px 2px 0 var(--pink-deep);display:flex;align-items:center;justify-content:center;text-align:center;font-family:var(--heading);font-size:10.5px;line-height:12px;color:var(--ink)}

.contact{position:absolute;left:0;top:844px;width:700px;height:293px;background:linear-gradient(90deg,#fbf9f8 0,#f1e7e1 45%,#eadbd2 65%,#f6f3f1 100%)}
.contact h2{position:absolute;left:107px;top:34px;font-family:var(--heading);font-weight:400;font-size:17px;color:var(--ink)}
.field{position:absolute;left:105px;width:138px;height:37px;background:var(--white);box-shadow:1px 1px 3px rgba(0,0,0,.15);padding:13px 12px;font-family:var(--heading);font-size:8.5px;color:var(--field-text)}
.field-message{width:219px;height:98px;padding-top:18px}
.submit{position:absolute;left:334px;top:239px;width:62px;height:27px;background:var(--pink);color:var(--white);font-family:var(--heading);font-size:10.5px;display:flex;align-items:center;justify-content:center}

.site-footer{position:absolute;left:0;top:1137px;width:700px;height:63px;background:var(--footer);color:var(--white);font-family:var(--nav);font-size:7px}
.site-footer a{position:absolute;top:23px;color:var(--white);text-decoration:none;white-space:nowrap}
.copyright{position:absolute;left:106px;top:38px}
.social{position:absolute;top:22px;width:18px;height:18px;border-radius:50%;background:var(--white)}
</style>
</head>
<body>
<div class="page">
  <nav class="site-nav">
    <a href="#home">HOME</a>
    <a href="#about">ABOUT US</a>
    <a href="#train">TRAIN@BRIMWELL PARLOUR</a>
    <a href="#work">WORK FROM HOME</a>
    <a href="#contact">CONTACT</a>
  </nav>

  <header class="hero" id="home">
    <div class="hero-photo" role="img" aria-label="Photo of a smiling woman in a red top beside a camera, warm bokeh lights behind"></div>
    <svg class="hero-panel" width="700" height="248" viewBox="0 0 700 248" aria-hidden="true">
      <defs><linearGradient id="panelFade" x1="0" x2="1"><stop offset="0" stop-color="#f2efee"/><stop offset="1" stop-color="#fbfafa"/></linearGradient></defs>
      <polygon points="0,0 240,0 322,248 0,248" fill="url(#panelFade)"/>
    </svg>
    <div class="brand-mark"></div>
    <div class="brand-name">Brimwell Parlour</div>
    <h1 class="hero-title">Welcome the<br>Brimwell Parlour,</h1>
    <p class="hero-sub">a unique Portal into the world of webcam modeling and chat hosting</p>
    <svg class="hero-arrow" style="left:300px" width="16" height="34" viewBox="0 0 16 34" aria-hidden="true"><polyline points="14,1 2,17 14,33" fill="none" stroke="rgba(255,255,255,.6)" stroke-width="1.2"/></svg>
    <svg class="hero-arrow" style="left:664px" width="16" height="34" viewBox="0 0 16 34" aria-hidden="true"><polyline points="2,1 14,17 2,33" fill="none" stroke="rgba(255,255,255,.6)" stroke-width="1.2"/></svg>
  </header>

  <section class="band band-pink about" id="about">
    <h2>About Us</h2>
    <p>Lorem ipsum dolor sit amet, consectetur adipisicing elit, sed do eiusmod tempor incididunt ut labore et dolore magna aliqua. Ut enim ad minim veniam, quis nostrud exercitation ullamco laboris nisi ut aliquip ex ea commodo consequat. Duis aute irure dolor in reprehenderit in voluptate velit esse cillum dolore eu fugiat nulla pariatur. Excepteur sint occaecat cupidatat non proident, sunt in culpa qui officia deserunt mollit anim id est laborum.</p>
  </section>

  <section class="band train" id="train">
    <div class="train-photo" role="img" aria-label="Faded photo of a woman on the phone at a desk with a laptop"></div>
    <h2>Train @ Brimwell Parlour</h2>
    <p>Lorem ipsum dolor sit amet, consectetur adipisicing elit, sed do eiusmod tempor incididunt ut labore et dolore magna aliqua. Ut enim ad minim veniam, quis nostrud exercitation ullamco laboris nisi ut aliquip ex ea commodo consequat. Duis aute irure dolor in reprehenderit in voluptate velit esse cillum dolore eu fugiat nulla pariatur. Excepteur sint occaecat cupidatat non proident, sunt in culpa qui officia deserunt mollit anim id est laborum.</p>
  </section>

  <section class="band band-pink work" id="work">
    <h2>Work From Home</h2>
    <p>Lorem ipsum dolor sit amet, consectetur adipisicing elit, sed do eiusmod tempor incididunt ut labore et dolore magna aliqua. Ut enim ad minim veniam, quis nostrud exercitation ullamco laboris nisi ut aliquip ex ea commodo consequat. Duis aute irure dolor in reprehenderit in voluptate velit esse cillum dolore eu fugiat nulla pariatur. Excepteur sint occaecat cupidatat non proident, sunt in culpa qui officia deserunt mollit anim id est laborum.</p>
    <div class="bubble" style="left:266px">What do I<br>need?</div>
    <div class="bubble" style="left:365px">How do I<br>sign up</div>
  </section>

  <section class="contact" id="contact" role="img" aria-label="Faded photo of a woman with long hair looking down">
    <h2>Contact Us</h2>
    <div class="field" style="top:71px">Enter your Name</div>
    <div class="field" style="top:117px">Enter your Mail Id</div>
    <div class="field field-message" style="top:163px">Enter your Message</div>
    <div class="submit">Submit</div>
  </section>

  <footer class="site-footer">
    <a style="left:106px" href="#about">About us</a>
    <a style="left:179px" href="#train">Train@Brimwell Parlour</a>
    <a style="left:278px" href="#work">Work from Home</a>
    <a style="left:377px" href="#contact">Contact</a>
    <div class="copyright">Copyright © 2014 Brimwell Parlour. All rights reserved.</div>
    <span class="social" style="left:521px"></span>
    <span class="social" style="left:539px"></span>
    <span class="social" style="left:558px"></span>
    <span class="social" style="left:576px"></span>
  </footer>
</div>
</body>
</html>
```